Architecture firm needing a business card

We need a business card design for a new company based in the US called "Pellmore Architecture". Seeking minimalist designs that have a creativity/design feel but must be clean and professional. Please refer to the logo attached.

Target Market(s)

Real Estate Investors, Home Builders and Construction Firms.

Industry/Entity Type

Architecture

Contact Information for Business Card

Standard US size business cards. Would like to have some sort of graphic on the back side of the card - nothing that is too loud but something that may catch your attention. More or less grayscale colors that are in line with the logo colors (navy and greys essentially). Additional colors maybe accepted if blended properly (earthtones), but might be difficult to accomplish and maintain the clean/minimalist look.

Requirements
Must have
• Clean Lines
Nice to have
• some sort of graphics, would like to have something creative on the back side of the card
Should not have
• nothing too busy, cluttered or overwhelming.

```html
<!DOCTYPE html>
<html lang="en">
<head>
<meta charset="utf-8">
<title>Pellmore Architecture – Business Card</title>
<link rel="stylesheet" href="https://fonts.googleapis.com/css2?family=Source+Sans+3:wght@300;400;600&display=swap">
<style>
  :root {
    --backdrop: #151515;
    --card: #ffffff;
    --navy: #1e4168;
    --ink: #3a3a3a;
    --grey: #8f8f8f;
  }
  * { margin: 0; padding: 0; box-sizing: border-box; }
  html, body {
    width: 1200px; height: 900px; overflow: hidden;
    background: var(--backdrop);
    font-family: "Source Sans 3", "Myriad Pro", sans-serif;
  }
  .stage { position: relative; width: 1200px; height: 900px; }
  .card {
    position: absolute; top: 170px;
    width: 347px; height: 561px;
    background: var(--card);
  }
  .card--front { left: 259px; }
  .card--back { left: 631px; }

  .band {
    position: absolute; left: 102px;
    width: 143px; height: 30px;
    background: var(--navy);
  }
  .band--top { top: 0; }
  .band--bottom { bottom: 0; }

  .wordmark {
    position: absolute; top: 276px; left: 0; width: 100%;
    text-align: center; color: var(--navy);
    font-weight: 400; text-transform: uppercase;
  }
  .front-mark {
    top: 92px;
    display: flex; flex-direction: column; align-items: center; gap: 14px;
    font-size: 26px; letter-spacing: 5px; line-height: 1.15;
  }
  .front-mark .square {
    width: 34px; height: 34px; background: var(--navy);
  }

  .identity {
    position: absolute; top: 294px; left: 0; width: 100%;
    text-align: center;
  }
  .identity .name {
    font-size: 19px; font-weight: 600; color: var(--navy); line-height: 24px;
  }
  .identity .role {
    font-size: 15px; color: var(--ink); line-height: 20px;
  }
  .address {
    position: absolute; top: 349px; left: 0; width: 100%;
    text-align: center; font-size: 15px; color: var(--ink); line-height: 20px;
    font-style: normal;
  }
  .contacts {
    position: absolute; top: 404px; left: 0; width: 100%;
    list-style: none; text-align: center;
    font-size: 15px; color: var(--ink); line-height: 20.5px;
  }
  .contacts svg {
    width: 10px; height: 10px; margin-right: 5px; vertical-align: -1px;
    fill: var(--navy);
  }

  .back-mark {
    position: absolute; left: 173px; top: 280px;
    display: flex; align-items: center; gap: 18px;
    transform: translate(-50%, -50%) rotate(-90deg);
    white-space: nowrap; color: var(--navy);
    font-size: 33px; font-weight: 400; letter-spacing: 4px; text-transform: uppercase;
  }
  .back-mark .square { width: 40px; height: 40px; background: var(--navy); }
</style>
</head>
<body>
<main class="stage">
  <section class="card card--front">
    <div class="band band--top"></div>

    <div class="wordmark front-mark">
      <span class="square"></span>
      <span>Pellmore<br>Architecture</span>
    </div>

    <div class="identity">
      <p class="name">Daniel Marsh</p>
      <p class="role">Managing Director</p>
    </div>

    <address class="address">
      4210, Linden Avenue<br>
      Portland, OR 97205.
    </address>

    <ul class="contacts">
      <li><svg viewBox="0 0 10 10" aria-hidden="true"><path d="M1 3.5C1 2 2.5 1.5 5 1.5S9 2 9 3.5V4.5H7V3.5H3V4.5H1Z"/><rect x="2" y="5" width="6" height="4" rx="0.8"/></svg>503-214 786 900</li>
      <li><svg viewBox="0 0 10 10" aria-hidden="true"><path d="M1 2.5H9V7.5H1Z"/><path d="M1 2.5L5 5.5L9 2.5" fill="none" stroke="#fff" stroke-width="0.9"/></svg>info@pellmore.com</li>
      <li><svg viewBox="0 0 10 10" aria-hidden="true"><g fill="none" stroke="#1e4168" stroke-width="1.4"><rect x="0.8" y="4.2" width="5" height="2.6" rx="1.3" transform="rotate(-45 3.3 5.5)"/><rect x="4.2" y="3.2" width="5" height="2.6" rx="1.3" transform="rotate(-45 6.7 4.5)"/></g></svg>www.pellmorearch.com</li>
    </ul>

    <div class="band band--bottom"></div>
  </section>

  <section class="card card--back">
    <div class="back-mark">
      <span class="square"></span>
      <span>Pellmore Architecture</span>
    </div>
  </section>
</main>
</body>
</html>
```